Web App Dashboard Design for Healthcare Company

We have developed a simple web application with 3 navigation menus. We like the current design (very much modeled after Ledgerly), but we want to explore UI options for the branding, header, menus, and footer that we may not have considered.

The attached screenshots show the layout and two menu "hover" views as they currently exist.

This web application is used by employees only.

Menu 1 - Module Menu:
Allows the user to switch easily between Account, Employee, and Care Management.

Menu 2 - Reports Menu
Allows user to view available reports within each Module.

Menu 3 - Admin Menu
Allows the user to easily create new content types within each module.

Use our branded colors and font.

Colors:
Logo Blue (dark): 00c0f3
Logo Blue (light): 44c8f5
Nav Blue: 0994d0
Green: 71b44b
Grayscale: (not specified)

Font:
Lato (Google Font)

Target Market(s)

Internal staff.

Industry/Entity Type

Healthcare

Number of Pages Required

3 page

Font styles to use
Sans Serif
Other font styles liked:
• Lato (Google Font)

Colors
0293ce
9bcb3c

Requirements
Must have
• It's really a one page design, but we want to see the two "hover" views for the Module Menu and the Admin Menu.
• It should also be very clear which "Report" page the user is on (the active menu link).
• Must use branded colors, font, and logo.
• Logo Blue (dark): 00c0f3
• Logo Blue (light): 44c8f5
• Nav Blue: 0994d0
• Green: 71b44b
• Grayscale: Designer may choose
Nice to have
• It would be nice to have simple uncluttered payouts.
Should not have
• The design should not have menu options exposed by default.

```html
<!DOCTYPE html>
<html lang="en">
<head>
<meta charset="utf-8">
<title>Carewell – Reminders</title>
<link href="https://fonts.googleapis.com/css2?family=Roboto:wght@400;500;700&display=swap" rel="stylesheet">
<style>
  :root {
    --page-bg: #edeef2;
    --white: #ffffff;
    --ink: #2e2e2e;
    --nav-top: #1a94d4;
    --nav-bottom: #0c80c2;
    --tab-active: #8bc06a;
    --brand-ink: #333333;
    --brand-dot: #0c80c2;
    --close-blue: #126ea6;
    --rule: #dcdde0;
    --head-bg: #f3f3f4;
    --pill-alert: #f88b8b;
    --pill-ok: #80fa8a;
    --action: #9c97f0;
    --action-soft: #aaa5f2;
    --footer-bg: #202020;
    --footer-ink: #ffffff;
  }
  * { box-sizing: border-box; margin: 0; padding: 0; }
  html, body { width: 1172px; height: 1200px; overflow: hidden; }
  body {
    position: relative;
    background: var(--page-bg);
    font-family: "Roboto", sans-serif;
    color: var(--ink);
  }

  /* Header */
  .app-header {
    position: absolute; left: 0; top: 0; width: 1172px; height: 87px;
    background: var(--white);
  }
  .brand {
    position: absolute; left: 43px; top: 30px;
    display: flex; align-items: center; gap: 8px;
  }
  .brand-dot { width: 12px; height: 12px; border-radius: 50%; background: var(--brand-dot); }
  .brand-name { font-size: 21px; font-weight: 400; color: var(--brand-ink); }

  .module-select {
    position: absolute; left: 218px; top: 23px; width: 286px; height: 39px;
    border: 1px solid #c9c9c9; border-radius: 20px;
    box-shadow: 0 1px 2px rgba(0,0,0,.15);
    display: flex; align-items: center; padding: 0 20px;
    font-size: 11px; color: #444; letter-spacing: .2px;
  }
  .module-select svg { margin-left: auto; }

  .user-links {
    position: absolute; top: 32px; left: 962px;
    display: flex; align-items: center; font-size: 14.5px; color: #6a6a6a;
  }
  .user-links .close-btn { margin-right: 23px; }
  .user-links a { color: inherit; text-decoration: none; margin-right: 27px; }

  .admin-menu {
    position: absolute; left: 906px; top: 61px; width: 131px; height: 116px;
    background: var(--white); border: 1px solid #cfcfcf;
    box-shadow: 0 1px 3px rgba(0,0,0,.12);
    padding: 11px 0 0 16px; z-index: 5;
    list-style: none; font-size: 12px; color: #333; line-height: 19.3px;
  }
  .admin-menu::before {
    content: ""; position: absolute; top: -7px; left: 64px;
    width: 12px; height: 12px; background: var(--white);
    border-left: 1px solid #cfcfcf; border-top: 1px solid #cfcfcf;
    transform: rotate(45deg);
  }

  /* Main nav */
  .main-nav {
    position: absolute; left: 0; top: 87px; width: 1172px; height: 44px;
    background: linear-gradient(var(--nav-top), var(--nav-bottom));
  }
  .main-nav ul { list-style: none; }
  .main-nav li {
    position: absolute; top: 0; height: 44px; line-height: 44px;
    font-size: 14.5px; color: var(--white); text-transform: uppercase;
  }
  .main-nav li.is-active {
    left: 43px; width: 150px; background: var(--tab-active); text-align: center;
  }

  /* Table */
  .reminder-card {
    position: absolute; left: 43px; top: 182px; width: 1088px; height: 856px;
    background: var(--white); border: 1px solid #d2d3d6; border-radius: 3px;
    box-shadow: 0 1px 2px rgba(0,0,0,.08); overflow: hidden;
  }
  .reminder-table { width: 100%; border-collapse: collapse; table-layout: fixed; }
  .reminder-table col.c1 { width: 250px; }
  .reminder-table col.c2 { width: 196px; }
  .reminder-table col.c3 { width: 165px; }
  .reminder-table col.c4 { width: 188px; }
  .reminder-table col.c5 { width: 149px; }
  .reminder-table thead th {
    height: 63px; background: var(--head-bg);
    font-weight: 400; font-size: 16.5px; text-align: left; color: #333;
  }
  .reminder-table thead th:first-child { padding-left: 46px; }
  .reminder-table thead th:nth-child(n+2) { padding-left: 2px; }
  .reminder-table td {
    height: 79.3px; font-size: 16.5px; color: #333;
    border-bottom: 1px solid var(--rule);
  }
  .reminder-table tr:last-child td { border-bottom: none; }
  .reminder-table td:first-child { padding-left: 30px; }
  .pill {
    display: inline-block; width: 160px; height: 34px; line-height: 34px;
    border-radius: 2px; text-align: center; font-size: 16.5px; color: #333;
  }
  .pill--alert { background: var(--pill-alert); }
  .pill--ok { background: var(--pill-ok); }
  .action-btn {
    display: inline-block; width: 90px; height: 34px; line-height: 34px;
    border-radius: 2px; text-align: center; background: var(--action); color: #333;
  }
  .action-btn--soft { background: var(--action-soft); }

  .view-more {
    position: absolute; left: 85px; top: 1067px;
    font-size: 17px; color: #555; display: flex; align-items: center; gap: 8px;
  }

  /* Footer */
  .app-footer {
    position: absolute; left: 0; top: 1133px; width: 1172px; height: 67px;
    background: var(--footer-bg); color: var(--footer-ink); font-size: 12.5px;
  }
  .app-footer .copyright { position: absolute; left: 44px; top: 26px; }
  .app-footer .contact { position: absolute; right: 49px; top: 24px; }
</style>
</head>
<body>

<header class="app-header">
  <div class="brand">
    <span class="brand-dot"></span>
    <span class="brand-name">Carewell</span>
  </div>

  <div class="module-select">
    ACCOUNTS MANAGEMENT
    <svg width="9" height="5" viewBox="0 0 9 5"><path d="M0 0h9L4.5 5z" fill="#333"/></svg>
  </div>

  <nav class="user-links">
    <svg class="close-btn" width="19" height="19" viewBox="0 0 19 19">
      <circle cx="9.5" cy="9.5" r="9.5" fill="var(--close-blue)"/>
      <path d="M6.3 6.3l6.4 6.4M12.7 6.3l-6.4 6.4" stroke="#fff" stroke-width="2.2" stroke-linecap="round"/>
    </svg>
    <a href="#">My Info</a>
    <a href="#">Logout</a>
  </nav>

  <ul class="admin-menu">
    <li>New</li>
    <li>Account</li>
    <li>Company Contact</li>
    <li>Note</li>
    <li>Message</li>
  </ul>
</header>

<nav class="main-nav">
  <ul>
    <li class="is-active">Reminders</li>
    <li style="left:228px">Accounts</li>
    <li style="left:378px">Patient Requests</li>
    <li style="left:585px">Reports</li>
    <li style="left:724px">My Company</li>
  </ul>
</nav>

<section class="reminder-card">
  <table class="reminder-table">
    <colgroup><col class="c1"><col class="c2"><col class="c3"><col class="c4"><col class="c5"><col></colgroup>
    <thead>
      <tr><th>Neque quisquam</th><th>Dolorem ipsum</th><th>Consectetur</th><th>Dolorem ipsum</th><th>Adipisci velit</th><th></th></tr>
    </thead>
    <tbody>
      <tr><td><span class="pill pill--alert">Porro quisquam</span></td><td>Dolorem ipsum</td><td>Quisquam</td><td>Established</td><td>Quisquam est</td><td><span class="action-btn">Ipsum</span></td></tr>
      <tr><td><span class="pill pill--alert">Porro quisquam</span></td><td>Dolorem ipsum</td><td>Quisquam</td><td>Established</td><td>Quisquam est</td><td><span class="action-btn">Ipsum</span></td></tr>
      <tr><td><span class="pill pill--alert">Porro quisquam</span></td><td>Dolorem ipsum</td><td>Quisquam</td><td>Established</td><td>Quisquam est</td><td><span class="action-btn action-btn--soft">Ipsum</span></td></tr>
      <tr><td><span class="pill pill--ok">Porro quisquam</span></td><td>Dolorem ipsum</td><td>Quisquam</td><td>Established</td><td>Quisquam est</td><td><span class="action-btn">Ipsum</span></td></tr>
      <tr><td><span class="pill pill--ok">Porro quisquam</span></td><td>Dolorem ipsum</td><td>Quisquam</td><td>Established</td><td>Quisquam est</td><td><span class="action-btn">Ipsum</span></td></tr>
      <tr><td><span class="pill pill--ok">Porro quisquam</span></td><td>Dolorem ipsum</td><td>Quisquam</td><td>Established</td><td>Quisquam est</td><td><span class="action-btn">Ipsum</span></td></tr>
      <tr><td><span class="pill pill--ok">Porro quisquam</span></td><td>Dolorem ipsum</td><td>Quisquam</td><td>Established</td><td>Quisquam est</td><td><span class="action-btn">Ipsum</span></td></tr>
      <tr><td><span class="pill pill--ok">Porro quisquam</span></td><td>Dolorem ipsum</td><td>Quisquam</td><td>Established</td><td>Quisquam est</td><td><span class="action-btn">Ipsum</span></td></tr>
      <tr><td><span class="pill pill--ok">Porro quisquam</span></td><td>Dolorem ipsum</td><td>Quisquam</td><td>Established</td><td>Quisquam est</td><td><span class="action-btn">Ipsum</span></td></tr>
      <tr><td><span class="pill pill--ok">Porro quisquam</span></td><td>Dolorem ipsum</td><td>Quisquam</td><td>Established</td><td>Quisquam est</td><td><span class="action-btn">Ipsum</span></td></tr>
    </tbody>
  </table>
</section>

<a class="view-more">View More
  <svg width="11" height="10" viewBox="0 0 11 10"><path d="M1 1l4 4-4 4M6 1l4 4-4 4" fill="none" stroke="#555" stroke-width="1.5"/></svg>
</a>

<footer class="app-footer">
  <span class="copyright">Copyright © 2017. All Rights Reserved</span>
  <span class="contact">Contact us</span>
</footer>

</body>
</html>
```